We are a small NZ based company looking to rebrand our eco chem free cleaning product Brisko

This product was launched in 2021. The brand and labeling were aimed at the consumer who cared that the cleaning products they bought into their home were not only effective but non-harmful to their families and the environment. The label was a little bohemian/ natural. We feel that the labels now need to be more chic and classy, They need to look stylish in a country cottage as well as a high end minimalist home. Colours need to be mute so as to fit with most decors.
We need help with font colour and type - layout and balance. Trigger/ pump colour.
I have attached photos of our current range and labels
A couple of mock ups we are working on - (struggling with )
A colour pallet
The two last PNG files are closer to where we want to end up but they are not really right.

The products are sold online only
Our website is www.brisko.co.nz
The Brand board that we had done sometime ago is that last file.
Most of the colours on the labels are ok - except the apricot on the foaming hand soap bottle and the colour on the all purpose bottle - neither of which we love.
The Fair Harbour bottles are closer to what we are thinking.
Canva Links
https://www.draftpad.example/design/QWRTyu12abc/pLmNoPqRsTuVwXyZ12AbCd/edit
https://www.draftpad.example/design/QWRTzk34def/hGfEdCbAzYxWvUtSr34EfG/edit
https://www.draftpad.example/design/QWRTmn56ghi/tRsQpOnMlKjIhGfE56HiJk/edit
https://www.draftpad.example/design/QWRTbv78jkl/mNbVcXzLkJhGfDsA78LmNo/edit

Target Market(s)

Mothers who care about the products they bring into there homes but also want the product to look good in the home

Industry/Entity Type

Cleaning products

Requirements
Must have
• Design must be chic - and be able to sit and look great in any modern bathroom or kitchen.

```html
<!DOCTYPE html>
<html lang="en">
<head>
<meta charset="utf-8">
<title>Brisko – Cleaning Range Labels</title>
<link href="https://fonts.googleapis.com/css2?family=Lato:wght@400;700&family=Montserrat:wght@400;500&display=swap" rel="stylesheet">
<style>
  :root {
    --bg: #f4f6f8;
    --label-bg: #e6eff4;
    --label-edge: #d3e0e8;
    --orange: #d7894a;
    --blue: #2b6f8c;
    --green: #2f8a66;
    --glass-sub: #2bb3a8;
  }
  * { box-sizing: border-box; margin: 0; padding: 0; }
  html, body { width: 1200px; height: 900px; overflow: hidden; }
  body {
    background: var(--bg);
    font-family: "Lato", sans-serif;
    position: relative;
  }
  .range {
    position: absolute;
    left: 90px; top: 190px;
    display: flex; gap: 60px;
  }
  .label {
    position: relative;
    width: 300px; height: 520px;
    background: linear-gradient(180deg, #eef4f8 0%, var(--label-bg) 100%);
    border: 1px solid var(--label-edge);
    border-radius: 6px;
    overflow: hidden;
  }
  .label__band {
    position: absolute; left: 0; bottom: 0;
    width: 300px; height: 260px;
  }
  .brand {
    position: absolute; left: 14px; bottom: 34px;
    display: flex; flex-direction: column; align-items: center; gap: 12px;
  }
  .brand__name {
    writing-mode: vertical-rl; transform: rotate(180deg);
    font-family: "Montserrat", sans-serif; font-weight: 500;
    font-size: 60px; line-height: 1; letter-spacing: 1px;
    color: var(--accent);
  }
  .brand__dot {
    width: 30px; height: 30px; border-radius: 50%;
    background: var(--accent);
  }
  .rule {
    position: absolute; left: 84px; bottom: 34px;
    width: 2px; height: 300px; background: var(--accent);
  }
  .tagline {
    position: absolute; left: 94px; bottom: 34px;
    writing-mode: vertical-rl; transform: rotate(180deg);
    font-family: "Montserrat", sans-serif; font-weight: 400;
    font-size: 15px; letter-spacing: 1.2px;
    color: var(--accent);
  }
  .product {
    position: absolute; left: 118px; right: 12px; top: 188px;
    text-align: center; color: var(--title);
  }
  .product__title {
    font-weight: 700; font-size: 20px; line-height: 1.2;
    text-transform: uppercase; letter-spacing: -0.2px;
  }
  .product__uses {
    margin-top: 12px; font-size: 10.5px; line-height: 1.35;
    color: var(--uses);
    white-space: nowrap;
  }
  .label--all-purpose { --accent: var(--orange); --title: var(--orange); --uses: var(--orange); }
  .label--bathroom { --accent: var(--blue); --title: var(--blue); --uses: var(--blue); }
  .label--glass { --accent: var(--green); --title: var(--green); --uses: var(--glass-sub); }
  .label--glass .product__uses { font-size: 9.5px; white-space: normal; }
</style>
</head>
<body>
<main class="range">

  <section class="label label--all-purpose">
    <svg class="label__band" viewBox="0 0 300 260" role="img" aria-label="Soft apricot flowing wave pattern band">
      <defs>
        <linearGradient id="band-orange" x1="0" y1="0" x2="1" y2="1">
          <stop offset="0" stop-color="#e9d8cb"/>
          <stop offset="0.5" stop-color="#e4a877"/>
          <stop offset="1" stop-color="#dfe6ea"/>
        </linearGradient>
      </defs>
      <polygon points="0,110 300,20 300,215 0,215" fill="url(#band-orange)" opacity="0.85"/>
    </svg>
    <div class="brand"><span class="brand__name">Brisko</span><span class="brand__dot"></span></div>
    <span class="rule"></span>
    <span class="tagline">NATURALLY GENTLE CLEAN</span>
    <div class="product">
      <h2 class="product__title">All Purpose<br>Cleaner</h2>
      <p class="product__uses">Surfaces | Stains | Grease | Grime</p>
    </div>
  </section>

  <section class="label label--bathroom">
    <svg class="label__band" viewBox="0 0 300 260" role="img" aria-label="Soft blue flowing wave pattern band">
      <defs>
        <linearGradient id="band-blue" x1="0" y1="0" x2="1" y2="1">
          <stop offset="0" stop-color="#9fd0ef"/>
          <stop offset="0.5" stop-color="#3aa6e0"/>
          <stop offset="1" stop-color="#b9dcef"/>
        </linearGradient>
      </defs>
      <polygon points="0,110 300,20 300,215 0,215" fill="url(#band-blue)" opacity="0.85"/>
    </svg>
    <div class="brand"><span class="brand__name">Brisko</span><span class="brand__dot"></span></div>
    <span class="rule"></span>
    <span class="tagline">NATURALLY GENTLE CLEAN</span>
    <div class="product">
      <h2 class="product__title">Bathroom<br>Cleaner</h2>
      <p class="product__uses">Shower | Bath | Toilet | Tiles | Grout</p>
    </div>
  </section>

  <section class="label label--glass">
    <svg class="label__band" viewBox="0 0 300 260" role="img" aria-label="Soft green flowing wave pattern band">
      <defs>
        <linearGradient id="band-green" x1="0" y1="0" x2="1" y2="1">
          <stop offset="0" stop-color="#b9e2cd"/>
          <stop offset="0.5" stop-color="#3fb57a"/>
          <stop offset="1" stop-color="#c8e8d8"/>
        </linearGradient>
      </defs>
      <polygon points="0,110 300,20 300,215 0,215" fill="url(#band-green)" opacity="0.85"/>
    </svg>
    <div class="brand"><span class="brand__name">Brisko</span><span class="brand__dot"></span></div>
    <span class="rule"></span>
    <span class="tagline">NATURALLY GENTLE CLEAN</span>
    <div class="product">
      <h2 class="product__title">Glass<br>Cleaner</h2>
      <p class="product__uses">Reflective Surfaces | Stainless<br>Steel | Windows | Glass</p>
    </div>
  </section>

</main>
</body>
</html>
```